Business Card Design

our business is purchasing, rehabbing and flipping homes. Design a house in the palm of a hand. This card is for a new company based in Georgia. So we buy homes that have been foreclosed, short sales,abandond, old homes and vacant homes.
We help improve the communities that we work in. We would like to see designs that use a black background with green accent and other colors that blend and don't take away from the logo and other important information.

Industry/Entity Type

Business

Contact Information for Business Card

Mavenbrook Holdings
Turning Old Doors Into New Starts
2738 Fenwick Lane
Duluth GA 30418
Office: 678-555-0192
mavenbrookholdingsllc.example

```html
<!DOCTYPE html>
<html lang="en">
<head>
<meta charset="utf-8">
<title>Mavenbrook Holdings – Business Card</title>
<link href="https://fonts.googleapis.com/css2?family=Arimo:wght@400&family=Cinzel:wght@400&family=Open+Sans:wght@400&display=swap" rel="stylesheet">
<style>
  :root {
    --backdrop: #e4e5e7;
    --card-black: #0d0d0d;
    --card-white: #f4f4f4;
    --accent-green: #45c585;
    --accent-blue: #2f86de;
    --text-light: #e9e9e9;
    --text-muted: #8a8a8a;
  }
  * { margin: 0; padding: 0; box-sizing: border-box; }
  html, body {
    width: 1200px;
    height: 840px;
    overflow: hidden;
    background: var(--backdrop);
  }
  .canvas {
    position: relative;
    width: 1200px;
    height: 840px;
  }
  .card {
    position: absolute;
    left: 100px;
    top: 134px;
    width: 1000px;
    height: 572px;
    background: var(--card-white);
    overflow: hidden;
    box-shadow: 0 18px 40px rgba(0,0,0,0.18);
  }
  .card-surface {
    position: absolute;
    inset: 0;
    width: 1000px;
    height: 572px;
  }
  .surface-black { fill: var(--card-black); }
  .surface-green { fill: var(--accent-green); }

  .brand {
    position: absolute;
    left: 372px;
    top: 196px;
  }
  .brand-mark {
    position: absolute;
    left: -138px;
    top: 62px;
    width: 40px;
    height: 40px;
    border-radius: 50%;
    background: var(--accent-blue);
  }
  .brand-name {
    font-family: "Cinzel", "Times New Roman", serif;
    font-weight: 400;
    font-size: 40px;
    letter-spacing: 1.5px;
    color: var(--text-light);
    text-transform: uppercase;
    white-space: nowrap;
  }
  .brand-tagline {
    margin-top: 2px;
    margin-left: 18px;
    font-family: "Open Sans", Arial, sans-serif;
    font-size: 17px;
    letter-spacing: 0.6px;
    color: var(--text-muted);
    white-space: nowrap;
  }

  .contact-list {
    position: absolute;
    left: 286px;
    top: 316px;
    list-style: none;
  }
  .contact-item {
    display: flex;
    align-items: center;
    height: 34px;
  }
  .contact-icon {
    width: 22px;
    height: 22px;
    margin-right: 22px;
    fill: none;
    stroke: var(--accent-blue);
    stroke-width: 2;
  }
  .contact-icon .solid { fill: var(--accent-blue); stroke: none; }
  .contact-text {
    font-family: "Arimo", Arial, sans-serif;
    font-size: 22px;
    color: var(--text-light);
    white-space: nowrap;
  }
</style>
</head>
<body>
<main class="canvas">
  <section class="card" aria-label="Mavenbrook Holdings business card">
    <svg class="card-surface" viewBox="0 0 1000 572" aria-hidden="true">
      <path class="surface-green" d="M0 0 H1000 V440 C870 470 700 520 560 572 H0 Z"/>
      <path class="surface-black" d="M0 0 H1000 V418 C860 452 690 505 520 572 H0 Z"/>
    </svg>

    <div class="brand">
      <span class="brand-mark" aria-hidden="true"></span>
      <h1 class="brand-name">Mavenbrook Holdings</h1>
      <p class="brand-tagline">Turning Old Doors Into New Starts</p>
    </div>

    <ul class="contact-list">
      <li class="contact-item">
        <svg class="contact-icon" viewBox="0 0 24 24" aria-hidden="true">
          <path class="solid" d="M6.6 10.8a15.1 15.1 0 0 0 6.6 6.6l2.2-2.2a1 1 0 0 1 1-.25 11.4 11.4 0 0 0 3.6.57 1 1 0 0 1 1 1V20a1 1 0 0 1-1 1A17 17 0 0 1 3 4a1 1 0 0 1 1-1h3.5a1 1 0 0 1 1 1c0 1.25.2 2.45.57 3.57a1 1 0 0 1-.25 1z"/>
        </svg>
        <span class="contact-text">678-555-0192</span>
      </li>
      <li class="contact-item">
        <svg class="contact-icon" viewBox="0 0 24 24" aria-hidden="true">
          <circle cx="12" cy="12" r="9"/>
          <ellipse cx="12" cy="12" rx="4" ry="9"/>
          <path d="M3 12h18M5 7h14M5 17h14"/>
        </svg>
        <span class="contact-text">mavenbrookholdingsllc.example</span>
      </li>
      <li class="contact-item">
        <svg class="contact-icon" viewBox="0 0 24 24" aria-hidden="true">
          <path class="solid" d="M12 2a5 5 0 0 0-5 5c0 3.8 5 9 5 9s5-5.2 5-9a5 5 0 0 0-5-5zm0 7a2 2 0 1 1 0-4 2 2 0 0 1 0 4z"/>
          <path d="M4 22l3-6h10l3 6z"/>
        </svg>
        <span class="contact-text">2738 Fenwick Lane Duluth GA 30418</span>
      </li>
    </ul>
  </section>
</main>
</body>
</html>
```